quillnest.com redesign with wireframes, white space and custom form are very important

Need a new two column design that will convert easily to mobile responsive. Lots of white space. Winning design will probably be based on header area and making the custom form stand out. I want the header to be very much like www.tamvorlo.com except the form not to go up into the header.
Here are some of the websites I really like:
www.brisketdoors.com
http://plinkaroofsdirect.com/
http://dorvikamplandings.com/

We buy homes for cash and close fast. Our target is a home seller who is desperate to sell quickly.
I have uploaded my really ugly wireframe and my logo. I also uploaded my photo for the about us box and a possible photo to use for the header.
The copy on the wireframe is what I will be using except for the about us box.

Here is the exact link for video to frame in the top left box.
https://vidnook.example/Qp39xatLbRr

Number of Pages Required

1 page

Font styles to use
Sans Serif

Colors
0592cd
85cae6
eaf1f7
fbee3d
ec1f27

Requirements
Must have
• Everything on wireframe.
• Must use Verdana font and nothing should be smaller than 12 point. Most should be in 14 point. (except maybe inside of form)

```html
<!DOCTYPE html>
<html lang="en">
<head>
<meta charset="utf-8">
<title>quillnest.com — Sell Your Home Fast</title>
<link rel="stylesheet" href="https://fonts.googleapis.com/css2?family=Open+Sans:wght@300;400;600;700&family=Questrial&display=swap">
<style>
:root{
  --black:#0b0b0b;
  --yellow:#f4e40f;
  --yellow-deep:#e6d300;
  --white:#ffffff;
  --text:#2b2b2b;
  --muted:#9a9a9a;
  --rule:#d9d9d9;
  --tick:#c9c9c9;
  --video:#e4e4f3;
  --panel:#ececec;
  --field:#f3f3f3;
}
*{box-sizing:border-box;margin:0;padding:0}
html,body{width:1200px;height:3318px;overflow:hidden;background:var(--white)}
body{position:relative;font-family:"Questrial",sans-serif;color:var(--text)}
.abs{position:absolute}

/* ---------- header ---------- */
.hero-photo{left:0;top:97px;width:1200px;height:475px;
  background:linear-gradient(180deg,#6f9ccc 0%,#a9c4de 30%,#d8d9d3 52%,#8a8a82 70%,#5a6a3e 88%,#6e7b46 100%)}
.hero-shapes{left:0;top:0;width:1200px;height:572px}
.brand{left:140px;top:38px;font-family:"Open Sans",sans-serif;font-weight:700;font-size:34px;color:var(--white);display:flex;align-items:center;gap:10px}
.brand-dot{width:18px;height:18px;background:var(--white)}
.main-nav{left:470px;top:58px;display:flex;gap:0;font-size:16px}
.main-nav a{color:var(--muted);text-decoration:none;position:absolute;white-space:nowrap}
.main-nav a.current{color:var(--text)}
.top-social{left:935px;top:6px;display:flex;gap:10px}
.top-social span{width:14px;height:14px;border-radius:50%;background:#c8c8c8}
.top-social span:first-child{background:var(--yellow-deep)}
.top-phone{left:935px;top:30px;font-size:15px;color:var(--muted);display:flex;align-items:center;gap:8px}
.hero-headline{left:69px;top:404px;width:440px;font-family:"Open Sans",sans-serif;font-weight:400;font-size:25px;line-height:31px;color:var(--black)}
.btn{display:flex;align-items:center;justify-content:center;background:var(--yellow);color:#6b6200;font-size:17px;letter-spacing:.5px;text-transform:uppercase}
.btn-sellnow{left:69px;top:503px;width:210px;height:34px;background:#b7ab0c;color:var(--white)}

.lead-form{left:644px;top:243px;width:473px;height:244px;background:var(--white)}
.lead-form h2{height:34px;background:var(--yellow);font-family:"Open Sans",sans-serif;font-weight:400;font-size:17px;color:var(--black);display:flex;align-items:center;justify-content:center}
.form-grid{display:grid;grid-template-columns:1fr 1fr;gap:8px;padding:8px 8px 0}
.form-grid .field{height:40px;background:var(--field);border:1px solid #e4e4e4;font-size:13px;color:#8c8c8c;padding:0 10px;display:flex;align-items:center}
.lead-form .submit{margin:10px 8px 0;height:34px;background:var(--black);color:var(--yellow);font-size:18px;display:flex;align-items:center;justify-content:center}

/* ---------- section type ---------- */
.section-title{left:0;width:1200px;text-align:center;font-family:"Open Sans",sans-serif;font-weight:400;font-size:40px;color:var(--text)}
.section-sub{left:0;width:1200px;text-align:center;font-size:15px;color:var(--muted);line-height:24px}
.rule{height:1px;background:var(--rule)}
.dots{display:flex;gap:5px}
.dots span{width:7px;height:7px;border-radius:50%;background:var(--yellow-deep)}
.dots span.soft{background:#f0e98a}

/* ---------- about ---------- */
.avatar{left:567px;top:627px;width:62px;height:62px;border-radius:50%;background:linear-gradient(180deg,#a0a9b3,#5d6a78)}

/* ---------- what we do ---------- */
.video-frame{left:160px;top:1006px;width:468px;height:245px;background:var(--video)}
.benefits{left:683px;top:1055px;list-style:none;font-size:16px;color:var(--muted)}
.benefits li,.reasons li{display:flex;align-items:center;gap:8px}
.benefits li{height:48px}
.tick{width:18px;height:14px;flex:none}

.intro-heading{left:180px;top:1352px;width:400px;font-family:"Open Sans",sans-serif;font-size:20px;line-height:25px;color:var(--black)}
.intro-body{left:180px;top:1438px;width:400px;font-size:15px;line-height:22px;color:var(--muted)}
.btn-readmore{left:180px;top:1634px;width:165px;height:40px;font-size:15px;box-shadow:0 3px 0 #c8b800}
.diamond-art{left:640px;top:1345px;width:360px;height:372px}

.help-photo{left:160px;top:1758px;width:451px;height:233px;background:linear-gradient(180deg,#0f1b2e 0%,#233b5c 55%,#3a3a3a 100%)}
.help-title{left:160px;top:1858px;width:451px;text-align:center;font-family:"Open Sans",sans-serif;font-weight:600;font-size:34px;color:var(--white)}
.help-sub{left:160px;top:1898px;width:451px;text-align:center;font-size:13px;color:#dadada}
.reasons-heading{left:644px;top:1762px;font-family:"Open Sans",sans-serif;font-size:20px;color:var(--black)}
.reasons{left:644px;top:1800px;list-style:none;font-size:16px;color:var(--muted)}
.reasons li{height:33.5px}

/* ---------- testimonials ---------- */
.quote-mark{left:393px;top:2158px;font-family:"Open Sans",sans-serif;font-size:46px;color:var(--muted)}
.quote-text{left:400px;top:2190px;width:440px;text-align:center;font-size:15px;line-height:22px;color:var(--muted)}
.quote-name{left:0;top:2256px;width:1200px;text-align:center;font-size:16px;line-height:22px;color:var(--text)}
.slider-arrow{top:2188px;width:20px;height:36px}

/* ---------- blog ---------- */
.blog-intro{left:152px;top:2461px;width:301px;height:243px;background:var(--panel);padding:22px 14px}
.blog-intro h3{font-family:"Open Sans",sans-serif;font-weight:400;font-size:18px;color:var(--black);border-bottom:2px solid var(--yellow);display:inline-block;padding-right:40px}
.blog-intro h3 span{color:var(--yellow-deep)}
.blog-intro p{margin-top:18px;font-size:12.5px;line-height:18px;color:#7d7d7d}
.blog-intro .more{position:absolute;left:14px;bottom:26px;font-size:12.5px;color:#7d7d7d}
.blog-intro .more b{color:var(--yellow-deep)}
.blog-card{top:2461px;width:301px;height:243px;background:linear-gradient(180deg,#3d3d3d 0%,#5a5650 60%,#2b2b2b 100%)}
.blog-card .caption{position:absolute;left:30px;right:30px;top:100px;text-align:center;font-size:14px;line-height:18px;color:var(--white)}
.blog-card .more{position:absolute;left:0;right:0;bottom:16px;text-align:center;font-size:12.5px;color:var(--white)}

/* ---------- contact ---------- */
.btn-contact{left:506px;top:2773px;width:160px;height:38px;font-size:16px}
.site-footer{left:0;top:2848px;width:1200px;height:423px;background:var(--black)}
.say-hi{left:517px;top:2888px;width:88px;height:88px}
.footer-label{left:166px;top:2948px;font-family:"Open Sans",sans-serif;font-size:16px;color:var(--white)}
.footer-field{left:166px;width:359px;background:var(--white);font-size:12.5px;color:#9a9a9a;padding:6px 8px}
.btn-send{left:415px;top:3183px;width:110px;height:36px;font-size:17px}
.contact-item{text-align:center;color:var(--white);font-size:15px;line-height:19px}
.copyright{left:160px;top:3282px;font-size:13px;color:var(--muted)}
</style>
</head>
<body>

<!-- Header -->
<header>
  <div class="abs hero-photo" role="img" aria-label="Photo of a single-storey suburban house with a lawn under a blue sky"></div>
  <svg class="abs hero-shapes" viewBox="0 0 1200 572" aria-hidden="true">
    <rect x="0" y="0" width="1200" height="97" fill="#ffffff"/>
    <polygon points="0,0 480,0 0,400" fill="#0b0b0b"/>
    <polygon points="0,330 210,195 520,572 0,572" fill="#f4e40f"/>
  </svg>
  <div class="abs brand"><span class="brand-dot"></span>quillnest.com</div>
  <nav class="abs main-nav">
    <a class="current" style="left:0">Sell Your Home</a>
    <a style="left:155px">How it works</a>
    <a style="left:288px">Stop foreclosure</a>
    <a style="left:445px">Probate</a>
    <a style="left:531px">Contact</a>
  </nav>
  <div class="abs top-social" aria-hidden="true"><span></span><span></span><span></span><span></span><span></span></div>
  <div class="abs top-phone">
    <svg width="14" height="14" viewBox="0 0 24 24"><path fill="#e6d300" d="M6.6 10.8a15 15 0 0 0 6.6 6.6l2.2-2.2c.3-.3.7-.4 1-.2 1.1.4 2.3.6 3.6.6.6 0 1 .4 1 1V20c0 .6-.4 1-1 1A17 17 0 0 1 3 4c0-.6.4-1 1-1h3.5c.6 0 1 .4 1 1 0 1.3.2 2.5.6 3.6.1.3 0 .7-.2 1z"/></svg>
    555-014-2277
  </div>
  <h1 class="abs hero-headline">SELL YOUR HOME FOR CASH IN 8 DAYS WE BUY HOUSES NATIONWIDE.</h1>
  <div class="abs btn btn-sellnow">Sell Now</div>

  <form class="abs lead-form">
    <h2>Yes, I want to sell my home fast!</h2>
    <div class="form-grid">
      <div class="field">Your Name</div>
      <div class="field">Your phone number</div>
      <div class="field">Your Email Address</div>
      <div class="field">Property Address</div>
      <div class="field">Asking price</div>
      <div class="field">Comments</div>
    </div>
    <div class="submit">SUBMIT</div>
  </form>
</header>

<!-- About -->
<section>
  <div class="abs avatar" role="img" aria-label="Portrait photo of the owner"></div>
  <h2 class="abs section-title" style="top:700px">ABOUT US</h2>
  <p class="abs section-sub" style="top:756px">Owned and operated in Orlando Florida since 2001. Oldest Continuous<br>operated website in country.</p>
  <div class="abs dots" style="left:596px;top:843px"><span></span></div>
  <div class="abs rule" style="left:171px;top:852px;width:858px"></div>
</section>

<!-- What we do -->
<section>
  <h2 class="abs section-title" style="top:888px">WHAT WE DO</h2>
  <p class="abs section-sub" style="top:950px">These are the benefits of selling your home to us.</p>
  <div class="abs video-frame" role="img" aria-label="Embedded video player">
    <svg style="position:absolute;left:204px;top:92px" width="62" height="62" viewBox="0 0 62 62" aria-hidden="true">
      <circle cx="31" cy="31" r="26" fill="none" stroke="#a3a3b6" stroke-width="5" stroke-dasharray="120 12"/>
      <polygon points="25,19 44,31 25,43" fill="#a3a3b6"/>
    </svg>
  </div>
  <ul class="abs benefits">
    <li><svg class="tick" viewBox="0 0 18 14"><path d="M1 7l5 5L17 1" fill="none" stroke="#c9c9c9" stroke-width="2"/></svg>You pick the closing date</li>
    <li><svg class="tick" viewBox="0 0 18 14"><path d="M1 7l5 5L17 1" fill="none" stroke="#c9c9c9" stroke-width="2"/></svg>You pay NO commissions or fees</li>
    <li><svg class="tick" viewBox="0 0 18 14"><path d="M1 7l5 5L17 1" fill="none" stroke="#c9c9c9" stroke-width="2"/></svg>You don't have to paint, clean or make repairs</li>
  </ul>
  <div class="abs rule" style="left:171px;top:1316px;width:858px"></div>
  <div class="abs dots" style="left:586px;top:1312px"><span class="soft"></span><span></span></div>

  <h3 class="abs intro-heading">Sell your home or house fast for cash to aprofessional investor company. We buy Houses and close quickly.</h3>
  <p class="abs intro-body">Selling a home on your own has never been easier. From Orlando to Greensboro - and all points in between- you can sell your home today without any hassles. Call 1-800-555-0184 or fill out the form below to get a written offer on your home in just 36 hours. Sell today online to people that care.</p>
  <div class="abs btn btn-readmore">Read More</div>
  <svg class="abs diamond-art" viewBox="0 0 360 372" role="img" aria-label="Collage of three house photos in diamond frames">
    <defs>
      <linearGradient id="houseA" x1="0" y1="0" x2="0" y2="1"><stop offset="0" stop-color="#9fb7d6"/><stop offset="1" stop-color="#c9b994"/></linearGradient>
      <linearGradient id="houseB" x1="0" y1="0" x2="0" y2="1"><stop offset="0" stop-color="#d5e4f2"/><stop offset="1" stop-color="#8f9b72"/></linearGradient>
      <linearGradient id="houseC" x1="0" y1="0" x2="0" y2="1"><stop offset="0" stop-color="#1f4fa8"/><stop offset="1" stop-color="#c88a4a"/></linearGradient>
    </defs>
    <polygon points="110,8 210,108 110,208 10,108" fill="url(#houseA)" stroke="#fff" stroke-width="4"/>
    <polygon points="250,8 350,108 250,208 150,108" fill="url(#houseB)" stroke="#fff" stroke-width="4"/>
    <polygon points="180,110 300,230 180,364 60,230" fill="url(#houseC)" stroke="#fff" stroke-width="4"/>
  </svg>

  <div class="abs help-photo" role="img" aria-label="Modern house lit up at night"></div>
  <p class="abs help-title">We Can Help.</p>
  <p class="abs help-sub">We help you sell your house fast at fair price.</p>
  <h3 class="abs reasons-heading">If you need to sell a home fast because of</h3>
  <ul class="abs reasons">
    <li><svg class="tick" viewBox="0 0 18 14"><path d="M1 7l5 5L17 1" fill="none" stroke="#c9c9c9" stroke-width="2"/></svg>Divorce or Bankruptcy</li>
    <li><svg class="tick" viewBox="0 0 18 14"><path d="M1 7l5 5L17 1" fill="none" stroke="#c9c9c9" stroke-width="2"/></svg>Foreclosure</li>
    <li><svg class="tick" viewBox="0 0 18 14"><path d="M1 7l5 5L17 1" fill="none" stroke="#c9c9c9" stroke-width="2"/></svg>Landlord problems - evictions with tenants</li>
    <li><svg class="tick" viewBox="0 0 18 14"><path d="M1 7l5 5L17 1" fill="none" stroke="#c9c9c9" stroke-width="2"/></svg>Inherited property in probate</li>
    <li><svg class="tick" viewBox="0 0 18 14"><path d="M1 7l5 5L17 1" fill="none" stroke="#c9c9c9" stroke-width="2"/></svg>Termites, mold, flood or fire damage.</li>
    <li><svg class="tick" viewBox="0 0 18 14"><path d="M1 7l5 5L17 1" fill="none" stroke="#c9c9c9" stroke-width="2"/></svg>Moving or can't afford mortgage payments</li>
  </ul>
  <div class="abs rule" style="left:171px;top:2060px;width:858px"></div>
  <div class="abs dots" style="left:583px;top:2056px"><span class="soft"></span><span></span><span class="soft"></span></div>
</section>

<!-- Testimonials -->
<section>
  <h2 class="abs section-title" style="top:2096px">SELLER TESTIMONIALS</h2>
  <span class="abs quote-mark">“</span>
  <p class="abs quote-text">I just wanted to thank you for buying my home in Winter Park. You made it fast and easy and kept me well informed the whole way.</p>
  <p class="abs quote-name">Delwin Harrock<br>Winter Park</p>
  <svg class="abs slider-arrow" style="left:144px" viewBox="0 0 20 36" aria-hidden="true"><path d="M18 2L3 18l15 16" fill="none" stroke="#d0d0d0" stroke-width="2"/></svg>
  <svg class="abs slider-arrow" style="left:1030px" viewBox="0 0 20 36" aria-hidden="true"><path d="M2 2l15 16L2 34" fill="none" stroke="#d0d0d0" stroke-width="2"/></svg>
  <div class="abs rule" style="left:171px;top:2378px;width:858px"></div>
  <div class="abs dots" style="left:575px;top:2374px"><span class="soft"></span><span class="soft"></span><span></span><span class="soft"></span></div>
</section>

<!-- Latest blog -->
<section>
  <article class="abs blog-intro">
    <h3>LATEST <span>BLOG</span></h3>
    <p>Plinka Roofs Direct is known for its famous makeover of old houses, now Plinka Roofs Direct has done a different type of makeover – its website! Through its updated website, you now have clearer communication and quicker access ..</p>
    <span class="more">READ MORE <b>→</b></span>
  </article>
  <article class="abs blog-card" style="left:459px" role="img" aria-label="Photo of a brick house at dusk">
    <p class="caption">Some of the cities where we buy houses. Not all are listed.</p>
    <span class="more">READ MORE →</span>
  </article>
  <article class="abs blog-card" style="left:766px" role="img" aria-label="Photo of a two-storey house at dusk">
    <p class="caption">We buy nice pretty houses and some ugly ones as well.</p>
    <span class="more">READ MORE →</span>
  </article>
</section>

<!-- Contact -->
<div class="abs btn btn-contact">Contact Us</div>
<svg class="abs" style="left:410px;top:2785px" width="130" height="150" viewBox="0 0 130 150" aria-hidden="true">
  <path d="M92 8 C40 14 30 60 48 110" fill="none" stroke="#555" stroke-width="12"/>
  <polygon points="30,104 70,104 52,140" fill="#555"/>
</svg>

<footer class="abs site-footer">
  <svg class="abs say-hi" style="top:40px;left:517px" viewBox="0 0 88 88" aria-hidden="true">
    <circle cx="44" cy="42" r="40" fill="#f4e40f"/>
    <polygon points="14,66 6,88 32,76" fill="#f4e40f"/>
    <text x="44" y="48" text-anchor="middle" font-family="Open Sans, sans-serif" font-weight="700" font-size="16" fill="#0b0b0b">SAY HI!</text>
  </svg>
  <p class="abs footer-label" style="top:100px">SEND US A MESSAGE</p>
  <div class="abs footer-field" style="top:135px;height:30px">NAME</div>
  <div class="abs footer-field" style="top:180px;height:30px">EMAIL</div>
  <div class="abs footer-field" style="top:224px;height:100px">MESSAGE</div>
  <div class="abs btn btn-send" style="top:335px">SEND</div>

  <svg class="abs" style="left:690px;top:108px" width="30" height="40" viewBox="0 0 30 40" aria-hidden="true"><path d="M15 0C7 0 1 6 1 14c0 10 14 26 14 26s14-16 14-26C29 6 23 0 15 0z" fill="#f4e40f"/><circle cx="15" cy="14" r="5" fill="#0b0b0b"/></svg>
  <p class="abs contact-item" style="left:620px;top:162px;width:170px">482 Marlow Ave<br>#310 Fernbrook, FL<br>30917</p>

  <svg class="abs" style="left:685px;top:256px" width="40" height="34" viewBox="0 0 40 34" aria-hidden="true"><rect x="1" y="6" width="38" height="27" fill="#ffffff"/><path d="M1 6l19 14L39 6" fill="none" stroke="#0b0b0b" stroke-width="2"/><rect x="12" y="0" width="16" height="10" fill="#f4e40f"/></svg>
  <p class="abs contact-item" style="left:610px;top:298px;width:190px">hello@quillnest.com</p>

  <svg class="abs" style="left:940px;top:115px" width="44" height="44" viewBox="0 0 24 24" aria-hidden="true"><path fill="#f4e40f" d="M6.6 10.8a15 15 0 0 0 6.6 6.6l2.2-2.2c.3-.3.7-.4 1-.2 1.1.4 2.3.6 3.6.6.6 0 1 .4 1 1V20c0 .6-.4 1-1 1A17 17 0 0 1 3 4c0-.6.4-1 1-1h3.5c.6 0 1 .4 1 1 0 1.3.2 2.5.6 3.6.1.3 0 .7-.2 1z"/></svg>
  <p class="abs contact-item" style="left:880px;top:175px;width:165px;font-size:19px">555-014-2277</p>

  <span class="abs" style="left:947px;top:252px;width:30px;height:30px;border-radius:50%;background:var(--yellow)"></span>
  <p class="abs contact-item" style="left:880px;top:303px;width:165px;font-size:14px">FOLLOW US</p>
</footer>

<p class="abs copyright">©2015 copyright quillnest.com</p>

</body>
</html>
```